Lable for farmmade cloudy Apple Juice

I need a Lable for Applejuice
Name of the Product "Apfelsaft Morgenrand"
The juice is handcrafted on my small fram in the apls of austria and the apples come out of a Garden in a Monestery.
So on the lable should be the text "aus dem Klostergarten vom Stift Wendau"

My Farm is called "Tranderhof"

This three parts should be on the lable also the two Logos if they fit, from my Farm and the one of the Monestary. They could be small too.

Other texts on the lable with a lettersize ox minimum 1.2mm for the small „x“ :
Ing. Markus Tobias Rehner
Anton Weidler Straße 15
6431 Brunnach
rehner-beispiel.at

L-24

mindestens haltbar bis Ende 09/..
nach dem Öffnen gekühlt lagern und alsbald verbrauchen

The volume oft the bottle must be in the minimum size of 4mm „1 Ltr.“

Lables i like from the style are also uploaded.

Target Market(s)

local Customer

Requirements
Must have
• must look modern
Should not have
• should not look old fashioned

```html
<!DOCTYPE html>
<html lang="de">
<head>
<meta charset="utf-8">
<title>Apfelsaft Morgenrand – Etikett</title>
<link rel="stylesheet" href="https://fonts.googleapis.com/css2?family=Bebas+Neue&family=Montserrat:wght@700&display=swap">
<style>
  :root {
    --label-black: #000000;
    --juice-yellow: #f6e000;
    --info-white: #ffffff;
  }
  html, body {
    margin: 0;
    padding: 0;
    overflow: hidden;
    background: var(--label-black);
  }
  .label {
    position: relative;
    width: 799px;
    height: 1200px;
    overflow: hidden;
    background: var(--label-black);
    font-family: "Montserrat", Arial, sans-serif;
    font-weight: 700;
  }
  .product-title {
    margin: 0;
    font-family: "Bebas Neue", "Oswald", sans-serif;
    font-weight: 400;
    color: var(--juice-yellow);
  }
  .product-title__line {
    position: absolute;
    left: 0;
    width: 100%;
    text-align: center;
    line-height: 1;
    white-space: nowrap;
  }
  .product-title__line--kind {
    top: 60px;
    font-size: 184px;
  }
  .product-title__line--variety {
    top: 227px;
    font-size: 172px;
  }
  .apple-art {
    position: absolute;
    left: 222px;
    top: 418px;
    width: 364px;
    height: 380px;
    border-radius: 48% 48% 46% 46% / 52% 52% 48% 48%;
    background: radial-gradient(ellipse at 62% 38%, #f6e000 0%, #c9b400 45%, #5a5000 85%, #1a1700 100%);
  }
  .farm {
    position: absolute;
    top: 825px;
    left: 0;
    width: 100%;
    text-align: center;
    color: var(--juice-yellow);
  }
  .farm__name {
    margin: 0;
    font-size: 42px;
    letter-spacing: 1px;
    line-height: 1.1;
  }
  .farm__origin {
    margin: 0;
    font-size: 31px;
    line-height: 38px;
  }
  .producer {
    position: absolute;
    top: 969px;
    left: 0;
    width: 100%;
    margin: 0;
    text-align: center;
    font-style: normal;
    font-size: 17.5px;
    line-height: 20px;
    color: var(--info-white);
  }
  .storage-note {
    position: absolute;
    top: 1079px;
    left: 101px;
    margin: 0;
    font-size: 17.5px;
    line-height: 20px;
    color: var(--info-white);
  }
  .volume {
    position: absolute;
    top: 1103px;
    right: 97px;
    margin: 0;
    font-size: 47px;
    line-height: 1;
    color: var(--info-white);
  }
</style>
</head>
<body>
  <main class="label">
    <h1 class="product-title">
      <span class="product-title__line product-title__line--kind">APFELSAFT</span>
      <span class="product-title__line product-title__line--variety">MORGENRAND</span>
    </h1>

    <div class="apple-art" role="img" aria-label="Gelbe Stichillustration eines Apfels mit Stiel und Blatt"></div>

    <section class="farm">
      <p class="farm__name">TRANDERHOF</p>
      <p class="farm__origin">aus dem Klostergarten<br>vom Stift Wendau</p>
    </section>

    <address class="producer">
      Ing. Markus Tobias Rehner<br>
      Anton Weidler Straße 15<br>
      6431 Brunnach<br>
      rehner-beispiel.at
    </address>

    <p class="storage-note">
      mindestens haltbar bis Ende 11/26<br>
      nach dem Öffnen gekühlt lagern<br>
      und ehebaldigst verbrauchen
    </p>

    <p class="volume">1 Ltr</p>
  </main>
</body>
</html>
```